Business Card & Letterhead Design

We a financial advice company based in Australia. We provide advice to wealthy farmers.

We are changing our business name FROM Brightmere Financial TO Calderstone Wealth and we need a new letterhead and double sided business card design

Attached is designs from our previous branding (Brightmere Financial) as it includes all the details we require on the new Calderstone Wealth business cards and letterhead.

```html
<!DOCTYPE html>
<html lang="en">
<head>
<meta charset="utf-8">
<title>Calderstone Wealth Letterhead</title>
<link href="https://fonts.googleapis.com/css2?family=Lato:wght@400;700&display=swap" rel="stylesheet">
<style>
  :root {
    --backdrop: #d9dadb;
    --paper: #ffffff;
    --ink: #2b2b2b;
    --ink-soft: #555a5d;
    --slate: #5c6b72;
    --silver: #a9abad;
    --ghost: #f1f0f1;
  }
  * { margin: 0; padding: 0; box-sizing: border-box; }
  html, body {
    width: 1200px; height: 1160px; overflow: hidden;
    background: var(--backdrop);
    font-family: 'Lato', sans-serif;
  }
  .letterhead {
    position: absolute; left: 204px; top: 20px;
    width: 792px; height: 1120px;
    background: var(--paper);
    box-shadow: 0 6px 24px rgba(0,0,0,.18);
    overflow: hidden;
  }
  .brand {
    position: absolute; left: 60px; top: 70px;
    display: flex; flex-direction: column; align-items: center;
  }
  .brand-mark {
    width: 54px; height: 54px; border: 3px solid var(--ink-soft);
    border-radius: 50%; margin-bottom: 8px;
  }
  .brand-name {
    font-size: 26px; font-weight: 400; letter-spacing: 1.5px;
    text-transform: uppercase; color: var(--ink-soft);
  }
  .brand-tagline {
    font-size: 10.5px; letter-spacing: 5.2px; color: #8a8e90;
    text-transform: uppercase; margin-top: 2px;
  }
  .contact {
    position: absolute; right: 52px; top: 62px;
    text-align: right; font-size: 13px; line-height: 1.32; color: var(--ink);
  }
  .contact p + p { margin-top: 14px; }
  .contact .icon-line { display: flex; justify-content: flex-end; align-items: center; gap: 5px; }
  .contact svg { width: 11px; height: 11px; fill: var(--ink-soft); }
  .ghost-circle {
    position: absolute; left: 220px; top: 700px;
    width: 360px; height: 360px; border: 6px solid var(--ghost); border-radius: 50%;
  }
  .footer-note {
    position: absolute; right: 52px; top: 830px;
    text-align: right; font-size: 13px; line-height: 1.3; color: var(--ink);
  }
  .footer-note .motto { color: var(--ink-soft); }
  .footer-note .rule { display: block; width: 22px; height: 1px; background: var(--ink); margin: 6px 0 14px auto; }
  .wave { position: absolute; left: 0; bottom: 0; width: 792px; height: 240px; }
  .slogan {
    position: absolute; right: 52px; bottom: 58px;
    font-size: 17px; font-weight: 700; color: var(--paper);
  }
</style>
</head>
<body>
<div class="letterhead">
  <div class="brand">
    <div class="brand-mark"></div>
    <div class="brand-name">Calderstone Wealth</div>
    <div class="brand-tagline">Strategic Financial Advice</div>
  </div>

  <div class="contact">
    <p>Harlow Investments Pty Ltd<br>ATF The Ashgrove Investment<br>Trust T/AS Brightmere Financial<br>ABN: 12 345 678 901<br>Corporate Authorised<br>Representative of Keystone<br>Financial Planning Limited</p>
    <p>Suite 4A, 18 Wattle St<br>Riverton QLD 4000<br>PO Box 1234</p>
    <p>Eastvale QLD 4000</p>
    <div>
      <div class="icon-line">(07) 3000 0101 <svg viewBox="0 0 24 24"><path d="M6.6 10.8a15 15 0 0 0 6.6 6.6l2.2-2.2c.3-.3.7-.4 1-.2 1.1.4 2.3.6 3.6.6.6 0 1 .4 1 1V20c0 .6-.4 1-1 1A17 17 0 0 1 3 4c0-.6.4-1 1-1h3.5c.6 0 1 .4 1 1 0 1.3.2 2.5.6 3.6.1.3 0 .7-.2 1z"/></svg></div>
      <div class="icon-line">(07) 3000 0102 <svg viewBox="0 0 24 24"><path d="M6 3h12v5H6zM4 9h16a2 2 0 0 1 2 2v6h-4v4H6v-4H2v-6a2 2 0 0 1 2-2zm4 7v3h8v-3z"/></svg></div>
      <div class="icon-line">hello@calderstonewealth.com.au <svg viewBox="0 0 24 24"><path d="M2 5h20v14H2zm2 2v.5l8 5 8-5V7l-8 5z"/></svg></div>
      <div class="icon-line">www.calderstonewealth.com.au <svg viewBox="0 0 24 24"><circle cx="12" cy="12" r="10"/></svg></div>
    </div>
  </div>

  <div class="ghost-circle"></div>

  <div class="footer-note">
    <span class="motto">A Referral Built Business</span>
    <span class="rule"></span>
    Keystone Financial Planning Limited<br>
    Australian Financial Services License Number 000000<br>
    Principal Address: 100 Market Lane<br>
    PO Box 5678 Southbank VIC 3000
  </div>

  <svg class="wave" viewBox="0 0 792 240" preserveAspectRatio="none" aria-hidden="true">
    <path d="M0 198 C180 210 300 180 420 130 C540 80 660 60 792 58 L792 76 C660 78 540 100 420 150 C300 198 180 222 0 212 Z" fill="var(--silver)"/>
    <path d="M0 205 C180 222 300 200 420 150 C540 100 660 82 792 80 L792 240 L0 240 Z" fill="var(--slate)"/>
  </svg>
  <div class="slogan">'Financial Peace of Mind'</div>
</div>
</body>
</html>
```